Scholarly Pathways - educational consulting

I am beginning an Scholarly Pathways business - focusing on Tribal (Native American Indian) Communities, but will work with anyone. I have work experience in K-12 and Higher Education. Special Education - transition from school to work. Advising and facilitating with academic skills in higher education. I have a BS - Special Education, Masters - Educational Administration and working on a PhD in Higher Education. Also completing PMB approved certification as an Academic Life Coach

Target Market(s)

K12 college bound students and parents, Kinfolk Crossings college bound students and families, special education college bound students and parents

Industry/Entity Type

Business

Contact Information for Business Card

Marnie Odell Fenwick. PO Box 417, Cushing, OK 74023. (918) 555-0293. marnie@scholarlypathways.example

Requirements
Must have
• Scholarly Pathways is the name of the business - Kinfolk Crossings is a focus area
Nice to have
• Tourquoise would be nice. I do not have a logo yet

```html
<!DOCTYPE html>
<html lang="en">
<head>
<meta charset="utf-8">
<title>Scholarly Pathways – Business Card</title>
<link rel="stylesheet" href="https://fonts.googleapis.com/css2?family=Open+Sans:wght@400;600&display=swap">
<style>
  :root {
    --backdrop: #3a322e;
    --card: #1b1b1c;
    --card-edge: #101011;
    --accent: #3aa3e3;
    --text: #f2f2f2;
    --muted: #8e8e8e;
    --divider: #3c3c3e;
  }
  * { box-sizing: border-box; margin: 0; padding: 0; }
  html, body {
    width: 1200px; height: 844px; overflow: hidden;
    background: var(--backdrop);
    font-family: "Open Sans", Arial, sans-serif;
  }
  .stage {
    position: relative; width: 1200px; height: 844px;
    display: flex; align-items: center; justify-content: center; gap: 50px;
  }
  .card {
    position: relative; width: 530px; height: 303px;
    background: var(--card);
    border: 1px solid var(--card-edge);
    border-radius: 3px;
    box-shadow: 0 12px 28px rgba(0,0,0,.45);
    overflow: hidden;
  }

  /* Contact side */
  .brand-block {
    position: absolute; left: 190px; top: 46px;
    width: 62px; height: 62px; background: var(--accent); border-radius: 6px;
  }
  .identity {
    position: absolute; left: 14px; top: 148px; width: 248px; text-align: right;
  }
  .identity .name { color: var(--text); font-weight: 600; font-size: 20px; line-height: 1.2; }
  .identity .role { color: var(--accent); font-size: 14px; margin-bottom: 12px; }
  .identity .address { color: var(--text); font-size: 15px; line-height: 1.3; }
  .divider {
    position: absolute; left: 276px; top: 130px; width: 1px; height: 118px; background: var(--divider);
  }
  .contacts {
    position: absolute; left: 289px; top: 132px; width: 230px; list-style: none;
  }
  .contacts li {
    display: flex; align-items: center; gap: 8px;
    color: var(--text); font-size: 11.5px; height: 26px; white-space: nowrap;
  }
  .contacts svg { flex: none; }

  /* Brand side */
  .wordmark {
    position: absolute; inset: 0;
    display: flex; align-items: center; justify-content: center; gap: 16px;
  }
  .wordmark .mark { width: 72px; height: 72px; background: var(--accent); border-radius: 5px; flex: none; }
  .wordmark .label {
    color: var(--accent); font-size: 30px; font-weight: 400; line-height: 1.1;
    letter-spacing: .5px; text-transform: uppercase;
  }
</style>
</head>
<body>
<main class="stage">
  <section class="card card-contact" aria-label="Business card, contact side">
    <div class="brand-block" aria-hidden="true"></div>
    <div class="identity">
      <p class="name">Marnie Odell Fenwick</p>
      <p class="role">Managing Director</p>
      <p class="address">PO Box 417,<br>Cushing, OK 74023</p>
    </div>
    <div class="divider"></div>
    <ul class="contacts">
      <li>
        <svg width="16" height="16" viewBox="0 0 16 16"><rect width="16" height="16" rx="2" fill="var(--accent)"/><path d="M4 5.5c0-1 1-1.5 4-1.5s4 .5 4 1.5v1H10V5.8H6v.7H4z M5 8h6l1 4H4z" fill="#fff"/></svg>
        (918) 555-0293
      </li>
      <li>
        <svg width="16" height="16" viewBox="0 0 16 16"><rect width="16" height="16" rx="2" fill="var(--accent)"/><rect x="5.5" y="3" width="5" height="10" rx="1" fill="#fff"/><rect x="6.5" y="4.2" width="3" height="6" fill="var(--accent)"/></svg>
        (918) 555-0417
      </li>
      <li>
        <svg width="16" height="16" viewBox="0 0 16 16"><rect width="16" height="16" rx="2" fill="var(--accent)"/><rect x="3.5" y="5" width="9" height="6.5" fill="#fff"/><path d="M3.5 5l4.5 3.6L12.5 5" fill="none" stroke="var(--accent)" stroke-width="1"/></svg>
        marnie@scholarlypathways.example
      </li>
      <li>
        <svg width="16" height="16" viewBox="0 0 16 16"><rect width="16" height="16" rx="2" fill="var(--accent)"/><path d="M6.5 9.5l3-3M7 5.5l1-1a2 2 0 013 3l-1 1M9 10.5l-1 1a2 2 0 01-3-3l1-1" fill="none" stroke="#fff" stroke-width="1.3" stroke-linecap="round"/></svg>
        www.scholarlypathways.example
      </li>
    </ul>
  </section>

  <section class="card card-brand" aria-label="Business card, brand side">
    <div class="wordmark">
      <span class="mark" aria-hidden="true"></span>
      <span class="label">Scholarly<br>Pathways</span>
    </div>
  </section>
</main>
</body>
</html>
```